Hi
Thank you for considering my job.

I need a layout design for a website. The design should preferably suit GainsFrame Sitecraft layout. Please design according to the attached LAYOUT.GIF

I already have a logo which I like but could be pushed to change if you have an exceptional design. Otherwise I would like to try to incorporate the jigsaw pieces in the design somehow.

Our company is based in Australia and called Parting Toolbox. We have developed a "Apart Pack" to assist both men and women going through divorce to prepare themselves adequately before the seek legal or financial advice to ensure they pay professionals for "advice" and not instructions on basic administration.

I hope the successful candidate will also be able to design a logo and squeeze page and all of the marketing images I will need to accompany The Apart Pack in a few weeks time, though it is not part of this job.

I have attached a very rough guide as to the types of elements and how I would like it to feel. I am not set on any of the fonts or general presentation at all. I feel comfortable with the colour scheme but again, open to ideas. Although the logo has the dark teal green background, I am not sure this works on the web page - open to ideas.

Some must haves:
a video on the front page
an opt in/members' login
link to Tarvello books sales (affiliate widget)
Disclaimer must be visible on first SCREEN

The website must portray a professional, trustworthy and up to date type image - similar to a law firm, accounting firm, bank or university. It must be clean and crisp, inviting and non-gender biased.

Please message me if you have any questions at all.

Thanks again.
Marguerite
Perth, Australia

Target Market(s)

Australian MEN AND WOMEN - 30 - 60 years middle to upper income earners

Industry/Entity Type

Accounting

Requirements
Must have
• Some must haves:
a video on the front page
an opt in/members' login

The website must portray a professional, trustworthy and up to date type image - similar to a law firm, accounting firm BUT SLIGHTLY MORE PEOPLE ORIENTED

```html
<!DOCTYPE html>
<html lang="en">
<head>
<meta charset="utf-8">
<title>Parting Toolbox – Home</title>
<link rel="stylesheet" href="https://fonts.googleapis.com/css2?family=Open+Sans:ital,wght@0,400;0,600;0,700;0,800;1,400;1,600;1,700;1,800&display=swap">
<style>
:root{
  --teal-dark:#0a4d56;
  --teal-deep:#06262b;
  --cyan:#3ccfe3;
  --aqua:#7ceaf8;
  --aqua-head:#5ee0f2;
  --orange:#ff6a3d;
  --orange-text:#ff5a1f;
  --lime:#c8f03c;
  --page:#ececec;
  --ink:#1a1a1a;
  --grey:#5a5a5a;
  --white:#ffffff;
}
*{box-sizing:border-box;margin:0;padding:0}
html,body{width:1200px;height:1182px;overflow:hidden}
body{position:relative;background:var(--page);font-family:"Open Sans",Arial,sans-serif;color:var(--grey)}
.abs{position:absolute}

/* header */
.site-header{left:0;top:0;width:1200px;height:120px;background:var(--teal-dark);overflow:hidden}
.header-accent{left:0;top:0}
.brand{left:140px;top:52px;display:flex;align-items:center;gap:10px;color:var(--white);font-size:25px;font-weight:400;line-height:1}
.brand-mark{width:22px;height:22px;background:var(--cyan);display:block}
.account{top:20px;display:flex;align-items:center;gap:7px;color:var(--teal-deep);font-size:13px}
.account.login{left:763px}
.account.register{left:850px}
.account-divider{left:834px;top:20px;width:1px;height:18px;background:#2aa9ba}
.search{left:762px;top:70px;width:299px;height:24px;background:var(--white);border:1px solid #9adbe4;display:flex;align-items:center;justify-content:space-between;padding:0 4px 0 5px}
.search span{font-size:11px;font-style:italic;font-weight:600;color:#666}

/* navigation */
.main-nav{left:0;top:120px;width:1200px;height:30px;background:var(--teal-deep)}
.nav-list{list-style:none;display:flex;position:absolute;left:138px;top:0;height:30px}
.nav-list li{font-size:12px;color:#e8f2f3;line-height:30px;padding:0 12px;margin-right:5px;position:relative;white-space:nowrap}
.nav-list li.active::after{content:"";position:absolute;left:0;right:0;bottom:0;height:3px;background:var(--orange)}

/* feature boxes */
.card{border:3px solid var(--white);box-shadow:0 3px 5px rgba(0,0,0,.12)}
.kit{left:138px;top:177px;width:298px;height:273px;background:var(--aqua)}
.kit-head{height:45px;background:var(--aqua-head);border-bottom:2px solid #2fc3d8;text-align:center;font-size:19px;font-weight:800;font-style:italic;color:var(--ink);line-height:44px}
.kit-intro{left:12px;top:60px;width:280px;font-size:11.5px;line-height:18px;color:#1f2a2c}
.kit-item{display:flex;align-items:center;gap:6px;font-size:12px;font-weight:700;font-style:italic;color:#163a40;line-height:18px}
.kit-note{left:40px;top:228px;width:255px;font-size:10.5px;font-style:italic;color:#1f2a2c;line-height:17px}
.tool{left:138px;top:464px;width:298px;height:79px;background:var(--teal-dark)}
.tool-title{left:20px;top:20px;color:var(--white);font-size:18px;font-weight:800;font-style:italic;line-height:19px}

.video{left:451px;top:177px;width:296px;height:366px;background:var(--orange)}
.video-head{height:45px;border-bottom:1px solid #ffb39a;text-align:center;font-size:17.5px;font-weight:800;font-style:italic;color:var(--ink);line-height:18.5px;padding-top:4px}
.video-copy{left:38px;top:55px;width:240px;font-size:11.5px;line-height:18px;color:var(--white)}
.video-frame{left:7px;top:170px;width:280px;height:157px;background:linear-gradient(135deg,#b9b5a6 0%,#8c8470 40%,#5b4f43 65%,#a99e90 100%)}
.video-bar{left:7px;top:327px;width:280px;height:29px;background:#1b1b1b}

.buy{left:764px;top:177px;width:297px;height:366px;background:var(--lime)}
.query-line{display:flex;align-items:center;gap:8px;font-size:16px;font-weight:700;font-style:italic;color:var(--teal-dark)}
.query-tag{left:228px;top:12px;font-size:16px;font-weight:700;font-style:italic;color:var(--teal-dark)}
.buy-split{left:0;top:155px;width:291px;border-top:1px dashed #8fb51c}
.book{left:12px;top:178px;width:86px;height:128px;background:linear-gradient(160deg,#4f88c7 0%,#4aa94b 55%,#2f7d30 100%);transform:skewY(-4deg)}
.buy-now{left:145px;top:172px;font-size:28px;font-weight:800;font-style:italic;color:#f23c1a}
.price{left:168px;top:215px;width:86px;height:86px;border-radius:50%;background:radial-gradient(circle at 40% 30%,#fff6a8,#ffd400 55%,#f0a800);text-align:center;color:var(--ink);font-weight:800;font-style:italic}
.price .cur{display:block;font-size:24px;line-height:26px;padding-top:8px}
.price .amt{display:block;font-size:27px;line-height:28px}
.buy-copy{left:8px;top:314px;width:220px;font-size:13px;font-style:italic;color:#1a2a1a;line-height:15.5px}

/* articles */
.section-title{font-size:16.5px;font-weight:700;color:#5b5b5b}
.articles-title{left:138px;top:578px}
.article{top:618px;width:290px}
.article h3{font-size:13px;font-weight:700;font-style:italic;color:var(--teal-dark);line-height:15px}
.article p{margin-top:6px;font-size:12.5px;line-height:18.2px;color:var(--grey)}
.article .views{margin-top:8px;font-size:12.5px;font-weight:600;color:var(--orange-text)}
.pager{left:1000px;top:576px}
.rule-soft{left:170px;top:780px;width:880px;height:2px;background:linear-gradient(90deg,transparent,#c9c9c9 20%,#c9c9c9 80%,transparent)}

/* community */
.community-title{left:136px;top:800px}
.join{top:837px;height:65px;display:flex;align-items:center;gap:10px;padding-left:14px;font-size:12.5px;font-weight:700;line-height:15.5px}
.join.member{left:140px;width:191px;background:var(--lime);color:#1d2a10;border:2px solid var(--white)}
.join.tools{left:346px;width:192px;background:#ff3d10;color:var(--white);border:2px solid var(--white)}
.join.forum{left:553px;width:193px;background:var(--cyan);color:var(--teal-deep);border:2px solid var(--white);padding-left:10px;gap:7px;font-size:11.5px;letter-spacing:-.2px;white-space:nowrap}
.testimonial-title{left:767px;top:800px}
.testimonial{left:763px;top:833px;width:297px;height:73px;background:#e0e0e0;padding:10px 12px;font-size:12.5px;line-height:18.2px;color:var(--grey)}
.testimonial-by{left:933px;top:914px;font-size:13px;font-weight:600;color:var(--orange-text)}
.rule{left:138px;top:958px;width:923px;height:1px;background:#d2d2d2}

/* disclaimer */
.disclaimer-title{left:137px;top:980px;font-size:17px;font-weight:400;color:#5b5b5b}
.disclaimer{left:140px;top:1012px;font-family:Arial,Helvetica,sans-serif;font-size:12px;font-weight:700;color:#000}

/* footer */
.footer-nav{left:0;top:1067px;width:1200px;height:30px;background:#e0e0e0}
.footer-nav .nav-list li{color:#6a6a6a}
.social{left:532px;top:1110px;display:flex;gap:7px}
.social span{width:29px;height:29px;border-radius:50%;background:#c9c9c9;display:block}
.copyright{left:0;width:1200px;top:1150px;text-align:center;font-size:11px;color:#8a8a8a}
</style>
</head>
<body>

<header class="abs site-header">
  <svg class="abs header-accent" width="1200" height="120" viewBox="0 0 1200 120" aria-hidden="true">
    <path d="M717 0H1200V120H646Z" fill="var(--cyan)"/>
  </svg>
  <div class="abs brand"><span class="brand-mark" aria-hidden="true"></span><span>Parting Toolbox</span></div>

  <div class="abs account login">
    <svg width="18" height="17" viewBox="0 0 18 17" aria-hidden="true"><circle cx="9" cy="5" r="4.5" fill="var(--teal-deep)"/><path d="M1 17C1 11 17 11 17 17Z" fill="var(--teal-deep)"/></svg>
    <span>Login</span>
  </div>
  <span class="abs account-divider"></span>
  <div class="abs account register">
    <svg width="19" height="19" viewBox="0 0 19 19" aria-hidden="true"><rect x="1.5" y="3.5" width="14" height="14" fill="none" stroke="var(--teal-deep)" stroke-width="2.2"/><path d="M7 12L17 2" stroke="var(--teal-deep)" stroke-width="3"/></svg>
    <span>Register</span>
  </div>
  <div class="abs search">
    <span>Search</span>
    <svg width="18" height="18" viewBox="0 0 18 18" aria-hidden="true"><circle cx="7" cy="7" r="5" fill="none" stroke="#555" stroke-width="2.4"/><path d="M11 11L16.5 16.5" stroke="#555" stroke-width="3"/></svg>
  </div>
</header>

<nav class="abs main-nav">
  <ul class="nav-list">
    <li class="active">HOME</li><li>CONSIDERING DIVORCE?</li><li>LEGAL PROCESS</li><li>PARENTING</li><li>PROPERTY &amp; FINANCE</li><li>COMMUNITY</li><li>TOOLS</li><li>FAQs</li><li>ABOUT US</li>
  </ul>
</nav>

<section class="abs card kit">
  <h2 class="kit-head">Try our Apart Pack</h2>
  <p class="abs kit-intro">Lorem ipsum dolor sit amet consectetur adipisicing elitsed do eiusmod tempor incididun.</p>
  <div class="abs kit-item" style="left:5px;top:117px">
    <svg width="34" height="46" viewBox="0 0 34 46" aria-hidden="true"><circle cx="17" cy="9" r="7.5" fill="none" stroke="#2a3a3e" stroke-width="2.5"/><path d="M3 45V30C3 22 31 22 31 30V45Z" fill="none" stroke="#2a3a3e" stroke-width="2.5"/><path d="M15 24H19L18 40H16Z" fill="#2a3a3e"/></svg>
    <span>Administration<br>Support</span>
  </div>
  <div class="abs kit-item" style="left:134px;top:117px">
    <svg width="50" height="50" viewBox="0 0 50 50" aria-hidden="true"><path d="M12 3H46V36L34 47H12Z" fill="none" stroke="#2a3a3e" stroke-width="2.5"/><path d="M3 38L24 22L30 28L9 44Z" fill="#2a3a3e"/></svg>
    <span>Documentation<br>Prepration</span>
  </div>
  <div class="abs kit-item" style="left:6px;top:184px">
    <svg width="32" height="46" viewBox="0 0 32 46" aria-hidden="true"><text x="16" y="40" text-anchor="middle" font-family="Open Sans,Arial,sans-serif" font-size="44" font-weight="800" fill="#2a3a3e">$</text></svg>
    <span>Finances<br>Support</span>
  </div>
  <div class="abs kit-item" style="left:134px;top:184px">
    <svg width="50" height="44" viewBox="0 0 50 44" aria-hidden="true"><circle cx="25" cy="11" r="10" fill="#2a3a3e"/><path d="M4 44C4 28 46 28 46 44Z" fill="#2a3a3e"/><path d="M23 27H27L26 38H24Z" fill="var(--aqua)"/></svg>
    <span>Professional<br>Advisor</span>
  </div>
  <p class="abs kit-note">Lorem ipsum dolor sit amet consectetur &nbsp;elitsed do eiusmod.</p>
</section>

<section class="abs card tool">
  <h2 class="abs tool-title">Try our Free<br>Divorce Tool</h2>
  <svg class="abs" style="left:204px;top:14px" width="52" height="52" viewBox="0 0 52 52" aria-hidden="true"><g stroke="var(--white)" stroke-width="5" stroke-linecap="round" fill="none"><path d="M8 44L30 22"/><path d="M44 44L20 20"/><path d="M12 10L22 3L30 11L20 18Z" fill="var(--white)"/><path d="M36 14A8 8 0 1 1 46 4"/></g></svg>
</section>

<section class="abs card video">
  <h2 class="video-head">Watch the video now to<br>discover what it’s all about...</h2>
  <p class="abs video-copy">Lorem ipsum dolor sit amet consectetur adipisicing elitsed do eiusmod tempor incididunt ut labore et dolore magna aliqua. Ut enim ad minim veniam, quis nostrud exercitation ullamco laboris nisi ut aliquip ex ea commodo consequat.</p>
  <div class="abs video-frame" role="img" aria-label="Video still: a woman with long curly hair outdoors in front of a building">
    <svg class="abs" style="left:116px;top:56px" width="54" height="54" viewBox="0 0 54 54" aria-hidden="true"><circle cx="27" cy="27" r="27" fill="rgba(0,0,0,.55)"/><path d="M21 16L39 27L21 38Z" fill="rgba(255,255,255,.85)"/></svg>
  </div>
  <div class="abs video-bar">
    <svg width="280" height="29" viewBox="0 0 280 29" aria-hidden="true">
      <rect x="0" y="0" width="280" height="4" fill="#555"/><rect x="0" y="0" width="132" height="4" fill="#d61d1d"/><circle cx="132" cy="2" r="5" fill="#eee"/>
      <rect x="22" y="11" width="3" height="10" fill="#bbb"/><rect x="28" y="11" width="3" height="10" fill="#bbb"/>
      <path d="M60 13H64L69 9V23L64 19H60Z" fill="#999"/>
      <text x="85" y="20" font-family="Open Sans,Arial,sans-serif" font-size="10" fill="#fff" font-weight="600">0:30</text>
      <text x="107" y="20" font-family="Open Sans,Arial,sans-serif" font-size="10" fill="#bbb">/ 2:10</text>
      <rect x="162" y="11" width="16" height="9" rx="2" fill="none" stroke="#bbb" stroke-width="1.5"/>
      <circle cx="191" cy="16" r="6" fill="none" stroke="#999" stroke-width="3"/>
      <rect x="212" y="12" width="14" height="8" fill="none" stroke="#bbb" stroke-width="1.5"/>
      <rect x="238" y="10" width="16" height="11" fill="none" stroke="#bbb" stroke-width="1.5"/>
      <path d="M262 10H266M262 10V14M276 10H272M276 10V14M262 22H266M262 22V18M276 22H272M276 22V18" stroke="#bbb" stroke-width="1.5"/>
    </svg>
  </div>
</section>

<section class="abs card buy">
  <div class="abs query-tag">Query?</div>
  <div class="abs query-line" style="left:44px;top:16px">
    <svg width="38" height="42" viewBox="0 0 38 42" aria-hidden="true"><path d="M19 1L36 7V20C36 30 28 38 19 41C10 38 2 30 2 20V7Z" fill="var(--teal-dark)"/><text x="19" y="29" text-anchor="middle" font-family="Open Sans,Arial,sans-serif" font-size="22" font-weight="800" fill="var(--lime)">?</text></svg>
    <span>ask a question</span>
  </div>
  <div class="abs query-line" style="left:44px;top:64px">
    <svg width="40" height="38" viewBox="0 0 40 38" aria-hidden="true"><circle cx="15" cy="9" r="8" fill="var(--teal-dark)"/><path d="M1 38C1 20 29 20 29 38Z" fill="var(--teal-dark)"/><path d="M32 24V36M26 30H38" stroke="var(--teal-dark)" stroke-width="4"/></svg>
    <span>expert answer</span>
  </div>
  <div class="abs query-line" style="left:48px;top:111px">
    <svg width="36" height="36" viewBox="0 0 36 36" aria-hidden="true"><circle cx="18" cy="18" r="15.5" fill="none" stroke="var(--teal-dark)" stroke-width="3"/><circle cx="12.5" cy="14" r="2.5" fill="var(--teal-dark)"/><circle cx="23.5" cy="14" r="2.5" fill="var(--teal-dark)"/><path d="M10 21C13 28 23 28 26 21" fill="none" stroke="var(--teal-dark)" stroke-width="3"/></svg>
    <span>accept if satisfied</span>
  </div>
  <div class="abs buy-split"></div>
  <div class="abs book" role="img" aria-label="Cover of a downloadable family guidebook in blue and green tones"></div>
  <div class="abs buy-now">Buy Now</div>
  <div class="abs price"><span class="cur">$</span><span class="amt">12.99</span></div>
  <p class="abs buy-copy">Download immediately.<br>This simple guide provides a<br>wealth of essential information.</p>
  <svg class="abs" style="left:222px;top:314px" width="24" height="24" viewBox="0 0 24 24" aria-hidden="true"><path d="M4 2L22 12L4 22Z" fill="#f04a2a"/></svg>
</section>

<h2 class="abs section-title articles-title">Most Popular Articles</h2>
<svg class="abs pager" width="62" height="24" viewBox="0 0 62 24" aria-hidden="true"><path d="M20 2L4 12L20 22" fill="none" stroke="#b5b5b5" stroke-width="4"/><path d="M42 2L58 12L42 22" fill="none" stroke="#b5b5b5" stroke-width="4"/></svg>

<article class="abs article" style="left:139px">
  <h3>Lorem ipsum dolor sit amet elitsed incididunt eiusmod Ut enim minim veniam.</h3>
  <p>Lorem ipsum dolor sit amet adipisicing elitsed do eiusmod tempor incididunt ut labore et dolore magna aliqua. Ut enim minim veniam, aliquip ex ea commodo consequat.</p>
  <div class="views">[378 views in Aug]</div>
</article>
<article class="abs article" style="left:458px">
  <h3>Lorem ipsum dolor sit amet elited incidunt eiusmod Ut enim minim veniam.</h3>
  <p>Lorem ipsum dolor sit amet adipisicing elitsed do eiusmod tempor incididunt ut labore et dolore magna aliqua. Ut enim minim veniam, aliquip ex ea commodo consequat.</p>
  <div class="views" style="margin-left:3px">[378 views in Aug]</div>
</article>
<article class="abs article" style="left:769px">
  <h3>Lorem ipsum dolor sit amet elited incidunt eiusmod Ut enim minim veniam.</h3>
  <p>Lorem ipsum dolor sit amet adipisicing elitsed do eiusmod tempor incididunt ut labore et dolore magna aliqua. Ut enim minim veniam, aliquip ex ea commodo consequat.</p>
  <div class="views" style="margin-left:3px">[378 views in Aug]</div>
</article>

<div class="abs rule-soft"></div>

<h2 class="abs section-title community-title">Join our community</h2>
<div class="abs join member">
  <svg width="38" height="24" viewBox="0 0 38 24" aria-hidden="true"><circle cx="9" cy="8" r="5" fill="#1d2a10"/><circle cx="29" cy="8" r="5" fill="#1d2a10"/><circle cx="19" cy="7" r="6" fill="#1d2a10"/><path d="M0 22C0 13 18 13 18 22Z M20 22C20 13 38 13 38 22Z M8 24C8 13 30 13 30 24Z" fill="#1d2a10"/></svg>
  <span>Free membership</span>
</div>
<div class="abs join tools">
  <svg width="22" height="30" viewBox="0 0 22 30" aria-hidden="true"><rect x="1" y="1" width="20" height="28" rx="2" fill="#2a1a14"/><rect x="4" y="4" width="14" height="6" fill="#ff3d10"/><g fill="#ff3d10"><rect x="4" y="13" width="3" height="3"/><rect x="9.5" y="13" width="3" height="3"/><rect x="15" y="13" width="3" height="3"/><rect x="4" y="18.5" width="3" height="3"/><rect x="9.5" y="18.5" width="3" height="3"/><rect x="15" y="18.5" width="3" height="3"/><rect x="4" y="24" width="3" height="3"/><rect x="9.5" y="24" width="3" height="3"/><rect x="15" y="24" width="3" height="3"/></g></svg>
  <span>Instant access to<br>calculators and<br>tools</span>
</div>
<div class="abs join forum">
  <svg width="26" height="26" viewBox="0 0 28 28" aria-hidden="true"><rect x="2" y="6" width="20" height="20" rx="2" fill="none" stroke="var(--teal-deep)" stroke-width="2.5"/><path d="M10 18L24 4" stroke="var(--teal-deep)" stroke-width="4"/></svg>
  <span>Anonymous and free<br>participation in support<br>and advice forums</span>
</div>

<h2 class="abs section-title testimonial-title">Client Testimonials</h2>
<blockquote class="abs testimonial">Lorem ipsum dolor sit amet adipisicing elitsed do eiusmod tempor amet incididunt ut labore et dolore magna aliqua. Ut enim minim</blockquote>
<svg class="abs" style="left:888px;top:905px" width="32" height="18" viewBox="0 0 32 18" aria-hidden="true"><path d="M0 0H32V18Z" fill="#e0e0e0"/></svg>
<div class="abs testimonial-by">Lorem Ipsum text</div>

<div class="abs rule"></div>

<h2 class="abs disclaimer-title">Disclaimer</h2>
<p class="abs disclaimer">Lorem ipsum dolor sit amet consectetur adipisicing elitsed do eiusmod tempor incididunt ut labore et dolore aliqua. Ut enim ad minim veniam, quis nostrud</p>

<footer>
  <nav class="abs footer-nav">
    <ul class="nav-list">
      <li>HOME</li><li>CONSIDERING DIVORCE?</li><li>LEGAL PROCESS</li><li>PARENTING</li><li>PROPERTY &amp; FINANCE</li><li>COMMUNITY</li><li>TOOLS</li><li>FAQs</li><li>ABOUT US</li>
    </ul>
  </nav>
  <div class="abs social" aria-label="Social links"><span></span><span></span><span></span><span></span></div>
  <p class="abs copyright">© 2013 - PartingToolbox. &nbsp; | &nbsp; Terms &amp; Privacy</p>
</footer>

</body>
</html>
```